Stonebrook Inc Ad Design, trying to attract new customers

Please see attached pictures and files for information
We are a Class A - Residential General Contractor in Lynchburg, VA with Master HVAC and Master PLUMBING Licenses. We focus on Water and Air Solutions for property owners.
We build, remodel, and repair homes
We do HVAC, including Humidity Control and Air Purification
We do Plumbing
We love to fix Water Leaks for Plumbing, Roof Leaks, Skylight Leaks, Basement Leaks, Foundation Leaks, Door and Window Leaks
We solve water and air issues on the outside of properties with custom structures, grading, and landscaping

Target Market(s)

Residential and Light Commercial property owners

Industry/Entity Type

Construction

Font styles to use
Other font styles liked:
• see cards

Colors
0054AA
0677BA
7BADD7
CADEEF
E8F1F8
00AB8E
00BBA5
67D7C9
C6EFE9
E9F9F6

Requirements
Must have
• See business cards
Nice to have
• see business cards
Should not have
• My name

```html
<!DOCTYPE html>
<html lang="en">
<head>
<meta charset="utf-8">
<title>Stonebrook Inc – Plumbing &amp; HVAC Ad</title>
<link rel="stylesheet" href="https://fonts.googleapis.com/css2?family=Anton&family=Exo+2:wght@600;800&family=Roboto+Condensed:wght@700&family=Roboto:wght@500&display=swap">
<style>
  :root {
    --stage: #8a8a8a;
    --white: #ffffff;
    --blue-deep: #0a3a78;
    --blue-mid: #0054AA;
    --blue-bright: #0aa6e6;
    --blue-brand: #0677BA;
    --green-dark: #056b3a;
    --green-light: #62a83d;
    --green-line: #8cc63f;
    --tick: #7ed321;
    --yellow: #dcf514;
    --seal-gold: #f0a830;
    --seal-edge: #e07f10;
  }
  * { margin: 0; padding: 0; box-sizing: border-box; }
  html, body { width: 1200px; height: 722px; overflow: hidden; background: var(--stage); }
  .ad {
    position: absolute; left: 99px; top: 109px;
    width: 1002px; height: 500px; overflow: hidden;
    background: var(--white);
  }
  .ad-bg { position: absolute; inset: 0; }
  .brand {
    position: absolute; left: 0; top: 14px; width: 486px; text-align: center;
  }
  .brand-mark {
    width: 64px; height: 64px; border-radius: 50%;
    background: var(--brand-mark, #2e9a3c); margin: 0 auto 10px;
  }
  .brand-name {
    font-family: "Roboto Condensed", sans-serif; font-weight: 700;
    font-size: 60px; letter-spacing: 5px; color: var(--blue-brand); line-height: 1;
  }
  .tagline {
    position: absolute; left: 28px; top: 236px;
    font-family: "Exo 2", sans-serif; font-weight: 800; font-size: 26px;
    line-height: 26px; color: var(--yellow);
  }
  .headline {
    position: absolute; left: 27px; top: 292px;
    font-family: "Anton", sans-serif; font-size: 56px; line-height: 57px;
    color: var(--white); text-transform: uppercase; letter-spacing: 0.5px;
  }
  .seal {
    position: absolute; left: 397px; top: 195px; width: 160px; height: 160px;
  }
  .services { position: absolute; left: 601px; top: 20px; width: 380px; list-style: none; }
  .service {
    position: relative; padding-left: 28px;
    font-family: "Roboto", sans-serif; font-weight: 500; font-size: 27px;
    line-height: 32px; color: var(--white); letter-spacing: -0.3px;
  }
  .service + .service { margin-top: 13px; }
  .service + .service::before {
    content: ""; position: absolute; left: 28px; top: -8px; width: 240px; height: 1px;
    background: linear-gradient(90deg, rgba(140,198,63,.7), rgba(140,198,63,0));
  }
  .service .tick { position: absolute; left: -12px; top: 4px; width: 25px; height: 25px; }
  .contact-phone {
    position: absolute; left: 28px; top: 420px; display: flex; align-items: center; gap: 20px;
    font-family: "Exo 2", sans-serif; font-weight: 600; font-size: 50px; color: var(--white);
    letter-spacing: 0.5px;
  }
  .contact-online {
    position: absolute; left: 505px; top: 418px;
    font-family: "Exo 2", sans-serif; font-weight: 600; font-size: 31px;
    line-height: 36px; color: var(--white);
  }
  .contact-online div { display: flex; align-items: center; gap: 12px; }
</style>
</head>
<body>
<main class="ad">
  <svg class="ad-bg" width="1002" height="500" viewBox="0 0 1002 500" aria-hidden="true">
    <defs>
      <linearGradient id="panelBlue" x1="0" y1="0" x2="1" y2="1">
        <stop offset="0" stop-color="#0a66b8"/>
        <stop offset="1" stop-color="#0a3a78"/>
      </linearGradient>
      <linearGradient id="waveBlue" x1="0" y1="0" x2="1" y2="1">
        <stop offset="0" stop-color="#0aa6e6"/>
        <stop offset="1" stop-color="#0677BA"/>
      </linearGradient>
    </defs>
    <path d="M522,0 H1002 V413 H540 L500,340 C548,250 562,120 522,0 Z" fill="url(#panelBlue)"/>
    <path d="M512,0 C554,120 546,250 492,338" fill="none" stroke="var(--green-line)" stroke-width="6"/>
    <path d="M520,0 C562,120 554,250 500,340" fill="none" stroke="#0a9ae0" stroke-width="5"/>
    <path d="M0,226 C120,200 260,205 410,265 L496,335 L540,413 H0 Z" fill="url(#waveBlue)"/>
    <path d="M0,226 C120,200 260,205 410,265 L496,335" fill="none" stroke="#5fb33c" stroke-width="4"/>
    <path d="M498,338 L542,413" fill="none" stroke="var(--green-line)" stroke-width="4"/>
    <rect x="0" y="413" width="1002" height="87" fill="var(--green-dark)"/>
    <polygon points="495,413 1002,413 1002,500 495,500 465,456" fill="var(--green-light)"/>
  </svg>

  <div class="brand">
    <div class="brand-mark"></div>
    <div class="brand-name">STONEBROOK</div>
  </div>

  <p class="tagline">“WE PUT WATER<br>&amp; AIR IN ITS PLACE”</p>
  <h1 class="headline">Class A RBC<br>Plumbing &amp; HVAC</h1>

  <svg class="seal" viewBox="0 0 160 160" role="img" aria-label="Licensed, bonded and insured seal">
    <circle cx="80" cy="80" r="78" fill="var(--seal-edge)"/>
    <circle cx="80" cy="80" r="70" fill="var(--seal-gold)"/>
  </svg>

  <ul class="services">
    <li class="service"><svg class="tick" viewBox="0 0 24 24" aria-hidden="true"><circle cx="12" cy="12" r="12" fill="var(--tick)"/><path d="M6.5,12.5 L10.5,16.5 L17.5,8" fill="none" stroke="#fff" stroke-width="3" stroke-linecap="round" stroke-linejoin="round"/></svg>Humidity Control/<br>Air Purification</li>
    <li class="service"><svg class="tick" viewBox="0 0 24 24" aria-hidden="true"><circle cx="12" cy="12" r="12" fill="var(--tick)"/><path d="M6.5,12.5 L10.5,16.5 L17.5,8" fill="none" stroke="#fff" stroke-width="3" stroke-linecap="round" stroke-linejoin="round"/></svg>Roof/Skylight Leaks</li>
    <li class="service"><svg class="tick" viewBox="0 0 24 24" aria-hidden="true"><circle cx="12" cy="12" r="12" fill="var(--tick)"/><path d="M6.5,12.5 L10.5,16.5 L17.5,8" fill="none" stroke="#fff" stroke-width="3" stroke-linecap="round" stroke-linejoin="round"/></svg>Basement /<br>Foundation Leaks</li>
    <li class="service"><svg class="tick" viewBox="0 0 24 24" aria-hidden="true"><circle cx="12" cy="12" r="12" fill="var(--tick)"/><path d="M6.5,12.5 L10.5,16.5 L17.5,8" fill="none" stroke="#fff" stroke-width="3" stroke-linecap="round" stroke-linejoin="round"/></svg>Drainage/Grading/<br>Landscaping</li>
    <li class="service"><svg class="tick" viewBox="0 0 24 24" aria-hidden="true"><circle cx="12" cy="12" r="12" fill="var(--tick)"/><path d="M6.5,12.5 L10.5,16.5 L17.5,8" fill="none" stroke="#fff" stroke-width="3" stroke-linecap="round" stroke-linejoin="round"/></svg>Custom Outdoor<br>Structures - Porches,<br>Decks, Sunroom, Gazebos</li>
  </ul>

  <div class="contact-phone">
    <svg width="26" height="36" viewBox="0 0 26 36" aria-hidden="true"><path d="M8,2 C3,4 1,10 2,18 C3,26 8,33 14,34 L18,28 L13,23 C10,20 9,15 10,11 L14,7 L10,1 Z" fill="none" stroke="#fff" stroke-width="2.5" stroke-linejoin="round"/></svg>
    <span>(434) 555-0187</span>
  </div>

  <div class="contact-online">
    <div><svg width="26" height="18" viewBox="0 0 26 18" aria-hidden="true"><rect x="1" y="1" width="24" height="16" fill="none" stroke="#fff" stroke-width="2"/><path d="M1,1 L13,11 L25,1" fill="none" stroke="#fff" stroke-width="2"/></svg>Contact@StonebrookVA.com</div>
    <div><svg width="24" height="24" viewBox="0 0 24 24" aria-hidden="true"><g fill="none" stroke="#fff" stroke-width="1.8"><circle cx="12" cy="12" r="10"/><ellipse cx="12" cy="12" rx="4.5" ry="10"/><path d="M2,12 H22 M4,6.5 H20 M4,17.5 H20"/></g></svg>www.BuiltByStonebrookVA.com</div>
  </div>
</main>
</body>
</html>
```